Thistle Croft B&B Business Card

This beautiful high-class B&B is looking for a business card that stands out from the rest. They are in the middle of the countryside, have chickens, geese and a dog. They also love bumble bees.

I was maybe thinking a rustic drawing / print of a bumble bee and a sketch of the house, I am not sure.. I quite like the feel of this... http://www.fenwick-mill.co.uk/

Industry/Entity Type

Business

Contact Information for Business Card

Thistle Croft
Bed & Breakfast
Holtwick, Ashcombe, Westshire, ZX4 7QR
01632 961847 | www.thistlecroft.co.uk

```html
<!DOCTYPE html>
<html lang="en">
<head>
<meta charset="utf-8">
<title>Thistle Croft B&amp;B – Business Cards</title>
<link href="https://fonts.googleapis.com/css2?family=Nunito:wght@400;600&display=swap" rel="stylesheet">
<style>
  :root {
    --backdrop: #d9d9d9;
    --card: #ffffff;
    --mat: #e4e5e7;
    --ink: #6f6f6f;
    --ink-soft: #8a8a8a;
    --sky: #6f9fd8;
    --roof: #b8473a;
    --stone: #cdbf94;
    --lawn: #4d7a2c;
    --lawn-dark: #1f3318;
  }
  * { box-sizing: border-box; margin: 0; padding: 0; }
  html, body {
    width: 1200px; height: 902px; overflow: hidden;
    background: var(--backdrop);
    font-family: "Nunito", sans-serif;
  }
  .canvas { position: relative; width: 1200px; height: 902px; }

  .spread {
    position: absolute;
    display: flex;
    box-shadow: 0 6px 14px rgba(0,0,0,0.12);
  }
  .spread--top { left: 450px; top: 40px; }
  .spread--bottom { left: 90px; top: 470px; }

  .panel { width: 330px; height: 390px; position: relative; }
  .panel--white {
    background: var(--card);
    display: flex; flex-direction: column; align-items: center;
  }
  .panel--mat { background: var(--mat); padding: 20px; }

  .photo { width: 100%; height: 100%; position: relative; }
  .photo--barn-front {
    background: linear-gradient(180deg, var(--sky) 0%, #b9cde4 28%, var(--roof) 34%, var(--stone) 45%, #bfae7c 62%, var(--lawn) 74%, #d9c9a0 84%, #cbb98c 100%);
  }
  .photo--barn-hens {
    background: linear-gradient(180deg, #3f6a2a 0%, var(--sky) 22%, var(--roof) 30%, var(--stone) 42%, #c7b58a 55%, var(--lawn) 66%, #3d5f25 80%, var(--lawn-dark) 100%);
  }

  .brand { margin-top: 90px; text-align: center; color: var(--ink); }
  .brand__row { display: flex; align-items: center; justify-content: center; gap: 10px; }
  .brand__dot { width: 10px; height: 10px; border-radius: 50%; background: var(--ink); }
  .brand__name {
    font-weight: 600; font-size: 30px; letter-spacing: 0.06em; text-transform: uppercase;
    white-space: nowrap;
  }
  .brand__tag {
    margin-top: 6px; font-size: 13px; letter-spacing: 0.22em; text-transform: uppercase;
    border-top: 1px solid var(--ink-soft); padding-top: 6px; display: inline-block;
  }

  .contact {
    margin-top: auto; margin-bottom: 62px;
    text-align: center; color: var(--ink); line-height: 1.45;
  }
  .contact__phone { font-size: 20px; letter-spacing: 0.06em; }
  .contact__web { font-size: 17px; letter-spacing: 0.03em; }
  .spread--top .contact { margin-bottom: 80px; }

  .address {
    position: absolute; left: 16px; right: 12px; bottom: 24px;
    color: #ffffff; font-size: 14px; letter-spacing: 0.01em;
    white-space: nowrap;
  }
</style>
</head>
<body>
<main class="canvas">

  <section class="spread spread--top" aria-label="Business card, version one">
    <div class="panel panel--white">
      <div class="brand">
        <div class="brand__row"><span class="brand__dot"></span><span class="brand__name">Thistle Croft</span></div>
        <span class="brand__tag">Bed &amp; Breakfast</span>
      </div>
      <div class="contact">
        <p class="contact__web">www.thistlecroft.co.uk</p>
      </div>
    </div>
    <div class="panel panel--mat">
      <div class="photo photo--barn-front" role="img" aria-label="Photograph of the stone barn with red tiled roof, arched window, gravel drive and summer sky"></div>
    </div>
  </section>

  <section class="spread spread--bottom" aria-label="Business card, version two">
    <div class="panel panel--mat">
      <div class="photo photo--barn-hens" role="img" aria-label="Photograph of two hens on the lawn in front of the stone barn">
        <p class="address">Holtwick, Ashcombe, Westshire, ZX4 7QR</p>
      </div>
    </div>
    <div class="panel panel--white">
      <div class="brand">
        <div class="brand__row"><span class="brand__dot"></span><span class="brand__name">Thistle Croft</span></div>
        <span class="brand__tag">Bed &amp; Breakfast</span>
      </div>
      <div class="contact">
        <p class="contact__phone">01632 961847</p>
        <p class="contact__web">www.thistlecroft.co.uk</p>
      </div>
    </div>
  </section>

</main>
</body>
</html>
```